Brightpath Tech Academy by graduating students from college in two years

Based on the logo design, create stationary and business cards for
Dr. Velimir T Osunde, CEO, (703) 482-1630
and Mirela Thorpe, Respresentative, (301) 557-2048
Address: 4417 Marbleton Lane, Wrenfield Station, VA 22061
Incorporate elelments of the logo

Target Market(s)

USA

Other font styles liked:
• match with the logo type style

```html
<!DOCTYPE html>
<html lang="en">
<head>
<meta charset="utf-8">
<title>Brightpath Tech Academy Letterhead</title>
<link href="https://fonts.googleapis.com/css2?family=Montserrat:wght@400;700&family=Questrial&display=swap" rel="stylesheet">
<style>
  :root {
    --navy: #0c2161;
    --gold: #f6c22f;
    --ink: #3a3a3a;
    --muted: #555555;
    --paper: #ffffff;
    --backdrop: #e4e4e4;
  }
  * { box-sizing: border-box; margin: 0; padding: 0; }
  html, body {
    width: 1200px; height: 960px; overflow: hidden;
    background: var(--backdrop);
  }
  .letterhead {
    position: absolute; left: 255px; top: 35px;
    width: 690px; height: 890px;
    background: var(--paper);
    box-shadow: 0 4px 18px rgba(0,0,0,0.18);
    overflow: hidden;
  }
  .letterhead__art { position: absolute; inset: 0; }
  .brand-seal {
    position: absolute; left: 46px; top: 8px;
    width: 150px; height: 150px; border-radius: 50%;
    background: var(--paper);
    display: flex; align-items: center; justify-content: center;
    text-align: center; padding: 22px;
  }
  .brand-seal__name {
    font-family: "Montserrat", sans-serif; font-weight: 700;
    font-size: 15px; line-height: 1.25; color: var(--navy);
  }
  .contact-block {
    position: absolute; left: 530px; top: 40px;
    padding-left: 10px; border-left: 1.5px solid var(--gold);
    font-family: "Montserrat", sans-serif; color: var(--muted);
    font-size: 9.5px; line-height: 1.3;
  }
  .contact-block__name {
    font-weight: 700; font-size: 12.5px; color: var(--navy); line-height: 1.25;
  }
  .contact-block__person + .contact-block__person { margin-top: 3px; }
  .contact-block__phone { display: flex; align-items: center; gap: 4px; }
  .contact-block__phone svg { width: 9px; height: 9px; fill: var(--gold); }
  .contact-block__address { margin-top: 3px; }
  .letter {
    position: absolute; left: 68px; top: 242px; width: 560px;
    font-family: "Questrial", sans-serif; color: var(--ink);
  }
  .letter__salutation {
    font-family: "Montserrat", sans-serif; font-weight: 700;
    font-size: 16px; color: var(--muted); margin-bottom: 14px;
  }
  .letter__para { font-size: 11.6px; line-height: 1.3; margin-bottom: 15px; }
  .letter__closing {
    font-family: "Montserrat", sans-serif; font-weight: 700;
    font-size: 9.5px; color: var(--muted); margin-top: 20px;
  }
  .letter__signature {
    width: 110px; height: 30px; margin: 16px 0 0 40px;
    background: linear-gradient(90deg, #d8d8d8, #c4c4c4);
    border-radius: 4px;
  }
</style>
</head>
<body>
  <main class="letterhead">
    <svg class="letterhead__art" viewBox="0 0 690 890" width="690" height="890" aria-hidden="true">
      <path class="band band--top-navy" d="M0 0 H690 V10 C470 16 190 52 0 128 Z" fill="var(--navy)"/>
      <path class="band band--top-gold" d="M0 138 C190 62 420 30 580 24 C410 36 200 74 0 156 Z" fill="var(--gold)"/>
      <path class="band band--bottom-navy" d="M690 738 C560 818 320 864 70 882 C330 860 570 814 690 752 Z" fill="var(--navy)"/>
      <path class="band band--bottom-gold" d="M690 766 C520 848 260 880 0 890 H690 Z" fill="var(--gold)"/>
    </svg>

    <div class="brand-seal">
      <span class="brand-seal__name">Brightpath Tech Academy</span>
    </div>

    <address class="contact-block">
      <div class="contact-block__person">
        <div class="contact-block__name">Dr. Velimir T Osunde</div>
        <div class="contact-block__role">CEO</div>
        <div class="contact-block__phone">
          <svg viewBox="0 0 24 24"><path d="M6.6 10.8a15 15 0 0 0 6.6 6.6l2.2-2.2a1 1 0 0 1 1-.25 11.4 11.4 0 0 0 3.6.57 1 1 0 0 1 1 1V20a1 1 0 0 1-1 1A17 17 0 0 1 3 4a1 1 0 0 1 1-1h3.5a1 1 0 0 1 1 1c0 1.25.2 2.45.57 3.6a1 1 0 0 1-.25 1z"/></svg>
          (703) 482-1630
        </div>
      </div>
      <div class="contact-block__person">
        <div class="contact-block__name">Mirela Thorpe</div>
        <div class="contact-block__role">Respresentative</div>
        <div class="contact-block__phone">
          <svg viewBox="0 0 24 24"><path d="M6.6 10.8a15 15 0 0 0 6.6 6.6l2.2-2.2a1 1 0 0 1 1-.25 11.4 11.4 0 0 0 3.6.57 1 1 0 0 1 1 1V20a1 1 0 0 1-1 1A17 17 0 0 1 3 4a1 1 0 0 1 1-1h3.5a1 1 0 0 1 1 1c0 1.25.2 2.45.57 3.6a1 1 0 0 1-.25 1z"/></svg>
          (301) 557-2048
        </div>
      </div>
      <div class="contact-block__address">4417 Marbleton Lane<br>Wrenfield Station VA 22061</div>
    </address>

    <article class="letter">
      <p class="letter__salutation">Dear Mr. Carver,</p>
      <p class="letter__para">Lorem ipsum dolor sit amet, consectetuer adipiscing elit, sed diam nonummy nibh euismod tincidunt ut laoreet dolore magna aliquam erat volutpat. Ut wisi enim ad minim veniam, quis nostrud exerci tationmcorper suscipit lobortis nisl ut aliquip ex ea commodo consequat. Duis autem vel eum iriure dolor in hendrerit in vulputate velit esse molestie consequat, vel illum dolore eu feugiat</p>
      <p class="letter__para">Rorem ipsum dolor sit amet, consectetuer adipiscing elit, sed diam nonummy nibh euismod tincidunt ut laoreet dolore magna aliquam erat volutpat. Ut wisi enim ad minim veniam, quis nostrud exerci tationmcorper suscipit lobortis nisl ut aliquip ex ea commodo consequat. Duis autem vel eum iriure dolor in hendrerit in vulputate velit esse molest</p>
      <p class="letter__para">Dorem ipsum dolor sit amet, consectetuer adipiscing elit, sed diam nonummy nibh euismod tincidunt ut laoreet dolore magna aliquam erat volutpat. Ut wisi enim ad minim veniam, quis nostrud exerci tationmcorper suscipit lobortis nisl ut aliquip ex ea commodo consequat. Duis autem vel eum iriure dolor in hendrerit in suscipit lobortis nisl ut aliquip ex ea commodo consequat. Duis autem vel eum iriure dolor in hendrerit in vulputate velit esse molestie consequat, vel illum</p>
      <p class="letter__para">Sorem ipsum dolor sit amet, consectetuer adipiscing elit, sed diam nonummy nibh euismod tincidunt ut laoreet dolore magna aliquam erat volutpat. Ut wisi enim ad minim veniam, quis nostrud exerci tationmcorper suscipit lobortis nisl ut aliquip ex ea commodo consequat. Duis autem vel eum iriure dolor in</p>
      <p class="letter__closing">Sincerely,</p>
      <div class="letter__signature" role="img" aria-label="Handwritten signature of the sender"></div>
    </article>
  </main>
</body>
</html>
```